Poster to inspire rural women around Australia!

We need a poster for our upcoming annual women's events in 2017. The poster will be used for every event this year (needs to be editable in Adobe suite of products) as a template sent to our event hosts around regional Australia. Our group will be hosting 3 events When the Doubters fall quiet / Can crafty neighbours lift each other? / Living with loss. We would like the design to be able to work across these 3 topics and to be clean, honest and use imagery which is meaningful for our target audience. Examples of previous posters attached.

Target Market(s)

'The Wanderers'; 30 - 60 year old women who live in regional Australia and have been removed from their normal conversations channels because of family (young or old).

Industry/Entity Type

Events

Font styles to use
Sans Serif

Colors
eda3c7
eaf2ce
f9d9e8
cadf82

Requirements
Must have
• A4 size poster
• Editable using Adobe products
• Organisation name - The Marrowbank Circle
• Event name, date, venue, time, booking details and price
Nice to have
• Our colours (themarrowbankcircle.com.au) green & pink
• tag line 'connecting women with conversation'

```html
<!DOCTYPE html>
<html lang="en">
<head>
<meta charset="utf-8">
<title>The Marrowbank Circle – When the Doubters Fall Quiet</title>
<link rel="stylesheet" href="https://fonts.googleapis.com/css2?family=Bebas+Neue&family=Oswald:wght@700&family=Roboto:wght@300;400;500&display=swap">
<style>
  :root {
    --pink: #eda3c7;
    --pink-deep: #e39cc0;
    --stripe: rgba(214, 140, 180, 0.18);
    --green: #cadf82;
    --cream: #ecdcce;
    --plum: #93677e;
    --mauve: #c184a3;
    --ring: #f3c6d6;
    --ink: #2f2a2d;
    --label: #6a4b5a;
    --white: #ffffff;
    --page: #ffffff;
  }
  * { margin: 0; padding: 0; box-sizing: border-box; }
  html, body { width: 1200px; height: 1200px; overflow: hidden; background: var(--page); }
  .canvas { position: relative; width: 1200px; height: 1200px; }
  .poster {
    position: absolute; left: 206px; top: 43px; width: 788px; height: 1114px;
    background:
      repeating-linear-gradient(-45deg, transparent 0 40px, var(--stripe) 40px 80px),
      linear-gradient(135deg, var(--pink) 0%, var(--pink-deep) 55%, var(--pink) 100%);
    overflow: hidden; font-family: "Roboto", sans-serif;
  }
  .rings { position: absolute; left: 0; top: 0; width: 788px; height: 1114px; }
  .org {
    position: absolute; left: 0; top: 30px; width: 100%; text-align: center;
    font-family: "Bebas Neue", sans-serif; font-weight: 400; color: var(--white);
    font-size: 41px; line-height: 40px; letter-spacing: 3px;
  }
  .org__line { display: block; }
  .price-badge {
    position: absolute; left: 47px; top: 92px; width: 144px; height: 144px;
    border-radius: 50%; background: var(--cream);
    display: flex; align-items: center; justify-content: center;
    font-family: "Oswald", sans-serif; font-weight: 700; font-size: 40px;
    color: var(--ink); letter-spacing: -1px;
  }
  .hero-art {
    position: absolute; left: 206px; top: 118px; width: 436px; height: 392px;
    background: linear-gradient(90deg, var(--green) 0%, var(--green) 28%, var(--plum) 42%, var(--mauve) 58%, var(--green) 74%);
    border-radius: 40% 46% 42% 48% / 34% 38% 52% 46%;
  }
  .title {
    position: absolute; left: 0; top: 518px; width: 100%; text-align: center;
    font-family: "Bebas Neue", sans-serif; font-weight: 400; color: var(--white);
    font-size: 100px; line-height: 92px; letter-spacing: 1px;
  }
  .tagline {
    position: absolute; left: 0; top: 706px; width: 100%; text-align: center;
    font-family: "Bebas Neue", sans-serif; color: var(--white);
    font-size: 41px; line-height: 44px; letter-spacing: 5px;
  }
  .details { position: absolute; left: 234px; top: 760px; width: 318px; }
  .details__row {
    height: 56px; display: flex; align-items: center; justify-content: center;
    font-size: 38px; color: var(--ink); letter-spacing: 1px;
    border-bottom: 1.5px solid var(--ink);
  }
  .details__row--first { height: 50px; }
  .booking {
    position: absolute; left: 0; top: 940px; width: 100%; text-align: center; color: var(--white);
  }
  .booking__label { font-weight: 500; font-size: 17px; line-height: 22px; letter-spacing: 2px; color: var(--label); }
  .booking__line { font-weight: 300; font-size: 17px; letter-spacing: 2px; line-height: 22.5px; }
  .social {
    position: absolute; left: 0; top: 1062px; width: 100%; text-align: center;
    font-weight: 500; font-size: 22px; line-height: 28px; color: var(--green); letter-spacing: 1px;
  }
</style>
</head>
<body>
<main class="canvas">
  <section class="poster">
    <svg class="rings" viewBox="0 0 788 1114" aria-hidden="true">
      <circle cx="418" cy="301" r="272" fill="none" stroke="var(--ring)" stroke-width="1.2"/>
      <circle cx="418" cy="301" r="240" fill="none" stroke="var(--ring)" stroke-width="1.2"/>
    </svg>

    <h2 class="org">
      <span class="org__line">The</span>
      <span class="org__line">Marrowbank Circle</span>
    </h2>

    <div class="price-badge">$45pp</div>

    <div class="hero-art" role="img" aria-label="Illustration: green map of Australia with a woman's profile silhouette in plum tones"></div>

    <h1 class="title">When the Doubters<br>Fall Quiet</h1>
    <p class="tagline">Connecting women with conversation</p>

    <div class="details">
      <div class="details__row details__row--first">02|02|2017</div>
      <div class="details__row">8 A.M. - 1 P.M.</div>
      <div class="details__row">Australia</div>
    </div>

    <div class="booking">
      <p class="booking__label">Booking Details</p>
      <p class="booking__line">marrowbankcircle.com.au/next events</p>
      <p class="booking__line">junetallis@marrowmail.com.au</p>
      <p class="booking__line">0491570156</p>
    </div>

    <p class="social">@marrowbankcircle</p>
  </section>
</main>
</body>
</html>
```